Landing Page für Persönlichkeitsquiz
Zielgruppe
Persönlichkeitsquiz für Menschen über 40 Jahren die bessere Entscheidungen treffen möchten.
Aufgabenstellung
Landinpage Design plus QUIZ ( 6 Schritte)
Vollständige Projektbeschreibung:
Projektbeschreibung
„Roaming Sideways QUIZ“
roamingsideways.example
- Responsive Design für mobile & website (Most users: mobile)
- Design wird Grundlage für spätere Website
Dieses Quiz wendet sich an Menschen über 40 Jahre, die ihre persönlichen Lebensziele besser erreichen möchten. Bitte denke daran, dass Menschen in unserem Alter schon schlechter sehen – also bitte eine gut lesbare & etwas größere Schrift verwenden!
Auftrag:
QUIZ mit mehreren Runden
Schritte des Quiz:
1. Landingpage
1.1 Video (youtube eingebunden)
1.2 Text
1.3 „Start Quiz“ Button
1.4 „Bekannt aus“ mit Logos von Medien in denen Marv Olden besprochen wurde.
1.5 Testimonials?
QUIZ (Popup)
2. Erste Runde: „Kille“ alle Antworten die Dich nicht interessieren. Total 64 Antworten.
2.1 Text mit Aufgabenbeschreibung „Kille“ alle Antworten die Dich nicht interessieren. Du hast zwei Minuten.“
2.2 Ein Button pro Antwort (wie bei Lernivo)
2.3 Zwei Buttons pro Reihe
2.4 Oben: Progress bar
2.5 Oben: Countdown clock, Restzeit: 2 Minuten
3. Zweite Runde: „Wähle max. 18 Antworten aus die überleben sollen.“
3.1 Text mit Aufgabenbeschreibung „Wähle max. 18 Antworten aus die überleben sollen.“
3.2 Ein Button pro Antwort (wie bei Lernivo)
3.3 Zwei Buttons pro Reihe
3.4 Oben: Progress bar
3.5 Oben: Countdown clock, Restzeit: 60 Sekunden
3.6 Zähler der noch verfügbaren Antworten. Hier: Noch 18, noch 17, noch 16.. etc.
4. Dritte Runde: „Nur 9 Antworten dürfen überleben. Go!“
4.1 Text mit „Nur 9 Antworten dürfen überleben. Go!“
4.2 Ein Button pro Antwort (wie bei Lernivo)
4.3 Zwei Buttons pro Reihe
4.4 Oben: Progress bar
4.5 Oben: Countdown clock, Restzeit 45 ..

```html
<!DOCTYPE html>
<html lang="de">
<head>
<meta charset="utf-8">
<title>Roaming Sideways Quiz</title>
<link href="https://fonts.googleapis.com/css2?family=Open+Sans:wght@400;600;700&display=swap" rel="stylesheet">
<style>
:root{
  --violet-light:#c46bd4;
  --violet-deep:#5a35b8;
  --accent:#c46bd4;
  --gold:#e8b13c;
  --pink:#f08fc8;
  --text:#333;
  --muted:#6b6b6b;
  --tile:#ececec;
  --grey-bg:#ebebeb;
  --white:#fff;
}
*{box-sizing:border-box;margin:0;padding:0}
html,body{width:1161px;height:1200px;overflow:hidden}
body{position:relative;font-family:"Open Sans",sans-serif;color:var(--text);background:var(--white)}
.abs{position:absolute}
.hero{left:0;top:0;width:1161px;height:550px;background:linear-gradient(100deg,var(--violet-light),var(--violet-deep));overflow:hidden}
.brand{left:85px;top:52px;color:var(--white);font-weight:700;font-size:17px;line-height:23px;letter-spacing:.3px}
.nav{top:80px;color:var(--white);font-size:13px;display:flex;align-items:center;gap:6px}
.hero-title{left:85px;top:192px;color:var(--white);font-weight:700;font-size:25px;line-height:34px;white-space:nowrap}
.hero-copy{left:85px;top:276px;color:var(--white);font-size:13px;line-height:17px;width:300px}
.btn{background:var(--gold);color:var(--white);font-weight:700;font-size:13px;border-radius:18px;display:flex;align-items:center;justify-content:center;gap:6px}
.hero-btn{left:85px;top:350px;width:130px;height:36px;justify-content:flex-start;padding-left:14px}
.art-bump{left:975px;top:117px;width:42px;height:42px;border-radius:50%;background:#b05fd0}
.art{left:993px;top:145px;width:83px;height:270px;background:var(--pink)}
.card{left:168px;top:112px;width:825px;height:416px;background:var(--white);border-bottom:4px solid var(--accent);box-shadow:0 4px 14px rgba(0,0,0,.12)}
.step{left:563px;top:94px;width:35px;height:35px;border-radius:50%;background:var(--accent);border:2px solid var(--white);color:var(--white);font-weight:700;font-size:15px;display:flex;align-items:center;justify-content:center}
.back{left:30px;top:22px;color:var(--gold);font-weight:700;font-size:14px;display:flex;align-items:center;gap:6px}
.timer{left:303px;top:22px;font-size:14px;display:flex;align-items:center;gap:6px}
.timer b{color:var(--accent)}
.timer .sep{width:1px;height:18px;background:#ddd;margin:0 4px}
.timer span{color:var(--muted)}
.done{right:30px;top:22px;color:var(--accent);font-weight:700;font-size:14px}
.bar{left:30px;top:58px;width:765px;height:11px;border-radius:6px;background:var(--tile);overflow:hidden}
.bar i{display:block;width:188px;height:100%;background:var(--accent);border-radius:6px}
.q-title{left:0;width:825px;top:92px;text-align:center;font-weight:700;font-size:21px;color:#666}
.q-sub{left:0;width:825px;top:121px;text-align:center;font-size:14px;color:var(--muted)}
.grid{left:167px;top:162px;width:491px;display:grid;grid-template-columns:241px 241px;gap:9px 9px}
.opt{height:47px;background:var(--tile);color:var(--muted);font-size:13px;display:flex;align-items:center;justify-content:space-between;padding:0 16px 0 10px}
.opt .box{width:15px;height:15px;background:var(--white)}
.opt.on{background:var(--accent);color:var(--white)}
.opt.on .box{display:flex;align-items:center;justify-content:center}
.scroll{left:687px;top:146px;width:6px;height:243px;border-radius:3px;background:#eee}
.scroll i{position:absolute;left:0;top:12px;width:6px;height:48px;border-radius:3px;background:var(--accent)}
.next{right:30px;top:360px;color:var(--gold);font-weight:700;font-size:14px;display:flex;align-items:center;gap:6px}
.sec-title{left:0;width:1161px;text-align:center;font-weight:700;font-size:15px;color:var(--text)}
.rule{left:561px;width:39px;height:3px;background:var(--accent)}
.circle-r{left:1117px;top:578px;width:166px;height:166px;border-radius:50%;background:linear-gradient(160deg,#9a4fcf,#5a35b8)}
.press{left:0;top:0;width:1161px}
.logos{left:118px;top:655px;width:932px;height:80px;display:flex;align-items:center;justify-content:space-between}
.logo{display:flex;align-items:center;gap:6px;font-weight:700;font-size:17px;color:#4a4a4a;white-space:nowrap}
.logo .sq{width:14px;height:14px;background:#4a4a4a}
.arrow-btn{width:18px;height:18px;border-radius:50%;background:var(--gold);display:flex;align-items:center;justify-content:center}
.grey{left:0;top:804px;width:1161px;height:352px;background:var(--grey-bg);overflow:hidden}
.circle-l{left:-120px;top:53px;width:166px;height:166px;border-radius:50%;background:linear-gradient(160deg,#b060d2,#6a3cc0)}
.t-card{top:109px;width:324px;height:153px;background:var(--white);border-bottom:4px solid var(--accent);box-shadow:0 2px 6px rgba(0,0,0,.06)}
.avatar{left:16px;top:17px;width:66px;height:66px;border-radius:50%;background:linear-gradient(135deg,#9a7a5e,#5b4a3c)}
.name{left:99px;top:31px;font-weight:700;font-size:13.5px}
.from{left:99px;top:53px;font-size:10px;color:var(--muted)}
.from b{color:var(--text);font-weight:700}
.quote{right:14px;top:12px}
.t-text{left:16px;top:95px;width:295px;font-size:11px;line-height:14.5px;color:#555}
.cta{left:518px;top:1094px;width:125px;height:36px}
.footer{left:0;top:1156px;width:1161px;height:44px;background:linear-gradient(100deg,var(--violet-light),var(--violet-deep));color:var(--white);font-size:11.5px}
.footer .copy{left:85px;top:14px}
.footer .links{right:87px;top:14px;display:flex;gap:32px}
</style>
</head>
<body>

<header class="abs hero">
  <div class="abs brand">ROAMING<br>SIDEWAYS</div>
  <div class="abs nav" style="left:940px">Deutsch
    <svg width="12" height="8" viewBox="0 0 12 8"><path d="M1 1l5 5 5-5" fill="none" stroke="#fff" stroke-width="1.8"/></svg>
  </div>
  <div class="abs nav" style="left:1036px">Fragen</div>

  <h1 class="abs hero-title">Herzlich willkommen<br>bei Roaming Sideways</h1>
  <p class="abs hero-copy">Lorem ipsum dolor sit amet, consetetur sadipscing elitr, sed diam nonumy eirmod tempor invidunt ut labore et dolore magna aliquyam erat, sed diam voluptua.</p>
  <div class="abs btn hero-btn">
    <svg width="12" height="12" viewBox="0 0 12 12"><path d="M1 6h9M6 2l4 4-4 4" fill="none" stroke="#fff" stroke-width="1.8"/></svg>Quiz starten
  </div>

  <div class="abs art-bump"></div>
  <div class="abs art" role="img" aria-label="Dekorative Illustration neben dem Quiz"></div>

  <section class="abs card">
    <div class="abs back">
      <svg width="17" height="17" viewBox="0 0 17 17"><circle cx="8.5" cy="8.5" r="8.5" fill="#e8b13c"/><path d="M10 5l-3.5 3.5L10 12" fill="none" stroke="#fff" stroke-width="1.8"/></svg>zurück
    </div>
    <div class="abs timer">
      <svg width="17" height="17" viewBox="0 0 17 17"><circle cx="8.5" cy="8.5" r="7.5" fill="none" stroke="#c46bd4" stroke-width="1.6"/><path d="M8.5 4v5l3 2" fill="none" stroke="#c46bd4" stroke-width="1.6"/></svg>
      <b>02 : 00</b><i class="sep"></i><span>Restzeit: 2 Minuten</span>
    </div>
    <div class="abs done">0 % komplett</div>
    <div class="abs bar"><i></i></div>

    <h2 class="abs q-title">„Kille“ alle Antworten die Dich nicht interessieren.</h2>
    <p class="abs q-sub">Du hast zwei Minuten.</p>

    <div class="abs grid">
      <div class="opt on">Lorem ipsum dela martime de.<span class="box"><svg width="11" height="9" viewBox="0 0 11 9"><path d="M1 4.5l3 3 6-6" fill="none" stroke="#c46bd4" stroke-width="2"/></svg></span></div>
      <div class="opt">Lorem ipsum dela martime de.<span class="box"></span></div>
      <div class="opt">Lorem ipsum dela martime de.<span class="box"></span></div>
      <div class="opt">Lorem ipsum dela martime de.<span class="box"></span></div>
      <div class="opt">Lorem ipsum dela martime de.<span class="box"></span></div>
      <div class="opt on">Lorem ipsum dela martime de.<span class="box"><svg width="11" height="9" viewBox="0 0 11 9"><path d="M1 4.5l3 3 6-6" fill="none" stroke="#c46bd4" stroke-width="2"/></svg></span></div>
      <div class="opt">Lorem ipsum dela martime de.<span class="box"></span></div>
      <div class="opt">Lorem ipsum dela martime de.<span class="box"></span></div>
    </div>
    <div class="abs scroll"><i></i></div>

    <div class="abs next">weiter
      <svg width="17" height="17" viewBox="0 0 17 17"><circle cx="8.5" cy="8.5" r="8.5" fill="#e8b13c"/><path d="M7 5l3.5 3.5L7 12" fill="none" stroke="#fff" stroke-width="1.8"/></svg>
    </div>
  </section>
  <div class="abs step">1</div>
</header>

<section class="abs press">
  <h2 class="abs sec-title" style="top:587px">Bekannt aus</h2>
  <div class="abs rule" style="top:615px"></div>
  <div class="abs circle-r"></div>
  <div class="abs" style="left:84px;top:687px"><div class="arrow-btn"><svg width="8" height="10" viewBox="0 0 8 10"><path d="M6 1L2 5l4 4" fill="none" stroke="#fff" stroke-width="1.8"/></svg></div></div>
  <div class="abs logos">
    <div class="logo"><span class="sq"></span>Blickpunkt</div>
    <div class="logo">Tagesfeder</div>
    <div class="logo">Nordwelle</div>
    <div class="logo">Kontinentfunk</div>
    <div class="logo">Radio Acht</div>
    <div class="logo">Westklang</div>
    <div class="logo"><span class="sq"></span>Kanal Zwei</div>
  </div>
  <div class="abs" style="left:1059px;top:686px"><div class="arrow-btn"><svg width="8" height="10" viewBox="0 0 8 10"><path d="M2 1l4 4-4 4" fill="none" stroke="#fff" stroke-width="1.8"/></svg></div></div>
</section>

<section class="abs grey">
  <div class="abs circle-l"></div>
  <h2 class="abs sec-title" style="top:45px">Was sagen andere zum Quiz</h2>
  <div class="abs rule" style="top:73px"></div>

  <article class="abs t-card" style="left:85px">
    <div class="abs avatar" role="img" aria-label="Porträtfoto von Selma Brandhof"></div>
    <div class="abs name">Selma Brandhof</div>
    <div class="abs from">aus&nbsp; <b>Berlin</b></div>
    <svg class="abs quote" width="19" height="19" viewBox="0 0 19 19"><path d="M9.5 2a7 6.5 0 1 1-3.6 12.1L2.5 16l1-3.6A7 6.5 0 0 1 9.5 2z" fill="none" stroke="#c46bd4" stroke-width="1.6"/></svg>
    <p class="abs t-text">Lorem ipsum dolor sit amet, consetetur sadipscing elitr, sed diam nonumy eirmod tempor invidunt ut labore et dolore magna aliquyam erat, sed diam voluptua.</p>
  </article>
  <article class="abs t-card" style="left:418px">
    <div class="abs avatar" role="img" aria-label="Porträtfoto von Jonas Feldkamp" style="background:linear-gradient(135deg,#5e7a45,#c43a34)"></div>
    <div class="abs name">Jonas Feldkamp</div>
    <div class="abs from">aus&nbsp; <b>Bayern</b></div>
    <svg class="abs quote" width="19" height="19" viewBox="0 0 19 19"><path d="M9.5 2a7 6.5 0 1 1-3.6 12.1L2.5 16l1-3.6A7 6.5 0 0 1 9.5 2z" fill="none" stroke="#c46bd4" stroke-width="1.6"/></svg>
    <p class="abs t-text">Lorem ipsum dolor sit amet, consetetur sadipscing elitr, sed diam nonumy eirmod tempor invidunt ut labore et dolore magna aliquyam erat, sed diam voluptua.</p>
  </article>
  <article class="abs t-card" style="left:752px">
    <div class="abs avatar" role="img" aria-label="Porträtfoto von Carla Lindquist" style="background:linear-gradient(135deg,#b8b2aa,#5c5a52)"></div>
    <div class="abs name">Carla Lindquist</div>
    <div class="abs from">aus&nbsp; <b>Hannover</b></div>
    <svg class="abs quote" width="19" height="19" viewBox="0 0 19 19"><path d="M9.5 2a7 6.5 0 1 1-3.6 12.1L2.5 16l1-3.6A7 6.5 0 0 1 9.5 2z" fill="none" stroke="#c46bd4" stroke-width="1.6"/></svg>
    <p class="abs t-text">Lorem ipsum dolor sit amet, consetetur sadipscing elitr, sed diam nonumy eirmod tempor invidunt ut labore et dolore magna aliquyam erat, sed diam voluptua.</p>
  </article>
</section>

<div class="abs btn cta">
  <svg width="12" height="12" viewBox="0 0 12 12"><path d="M1 6h9M6 2l4 4-4 4" fill="none" stroke="#fff" stroke-width="1.8"/></svg>Quiz starten
</div>

<footer class="abs footer">
  <div class="abs copy">© Roaming Sideways QUIZ</div>
  <nav class="abs links"><span>Impressum</span><span>Datenschutz</span><span>Sitemap</span></nav>
</footer>

</body>
</html>
```